Business Card Design Project

I am looking for a double sided business card design that is bold on one side with creative use of the logo, but clean and professional looking on the other side with the contact information provided.

Target Market(s)

My target market is recruitment agents, senior managers of multinational companies. The target segments are finance and I.T.

Industry/Entity Type

Business

Requirements
Must have
• Double sided. Use provided logo.

Information to include, but use your creativity for the tags (example):
Name (Marcus Feldane)
Position (Director)
Mobile (+44 7XXXXXXXXX)
Phone (+44 20XXXXXXXX)
Email (marcus@wendlebymarsh.com)
Website (www.wendlebymarsh.com)

```html
<!DOCTYPE html>
<html lang="en">
<head>
<meta charset="utf-8">
<title>Wendleby Marsh Consulting – Business Card</title>
<link rel="stylesheet" href="https://fonts.googleapis.com/css2?family=Libre+Baskerville&family=Open+Sans:wght@400;600&display=swap">
<style>
  :root {
    --brand-blue: #1b4f93;
    --brand-green: #8dc63f;
    --ink: #2b2b2b;
    --paper: #ffffff;
    --backdrop: #e9eaec;
  }
  * { box-sizing: border-box; margin: 0; padding: 0; }
  html, body {
    width: 1200px; height: 936px; overflow: hidden;
    background: var(--backdrop);
  }
  .canvas {
    position: relative; width: 1200px; height: 936px;
    display: flex; flex-direction: column; align-items: center;
    justify-content: space-between; padding: 38px 0;
  }
  .card {
    position: relative; width: 720px; height: 411px; overflow: hidden;
    box-shadow: 0 4px 14px rgba(0,0,0,0.12);
  }

  /* Back side */
  .card--back { background: var(--brand-blue); }
  .card--back .wordmark {
    position: absolute; left: 430px; top: 150px;
    color: var(--paper);
  }

  /* Shared wordmark */
  .wordmark {
    display: flex; align-items: center; gap: 12px;
    font-family: "Libre Baskerville", Georgia, serif;
    font-size: 17px; line-height: 1.35; letter-spacing: 0.5px;
    text-transform: uppercase;
  }
  .wordmark__dot {
    width: 34px; height: 34px; border-radius: 50%;
    background: var(--brand-green); flex: none;
  }

  /* Front side */
  .card--front { background: var(--paper); }
  .card--front .wordmark {
    position: absolute; left: 440px; top: 95px;
    color: var(--brand-blue);
  }
  .accent-marks {
    position: absolute; left: 44px; top: 208px; width: 34px; height: 30px;
  }
  .accent-marks__green {
    position: absolute; left: 12px; top: 0; width: 16px; height: 22px;
    background: var(--brand-green);
  }
  .accent-marks__blue {
    position: absolute; left: 0; top: 6px; width: 20px; height: 24px;
    background: var(--brand-blue);
  }
  .person {
    position: absolute; left: 96px; top: 178px;
  }
  .person__name {
    font-family: "Libre Baskerville", Georgia, serif;
    font-size: 21px; color: var(--ink);
  }
  .person__role {
    font-family: "Open Sans", Arial, sans-serif;
    font-size: 13px; color: var(--brand-blue); margin-top: 4px; letter-spacing: 0.3px;
  }
  .contact-list {
    position: absolute; left: 150px; top: 258px; list-style: none;
    font-family: "Open Sans", Arial, sans-serif; font-size: 13.5px; color: var(--ink);
  }
  .contact-list li { display: flex; align-items: center; height: 21px; }
  .contact-list__tag {
    width: 14px; color: var(--brand-blue); font-weight: 600;
  }
  .contact-list__sep {
    width: 2px; height: 11px; background: var(--brand-green); margin: 0 9px 0 2px;
  }
  .band-blue {
    position: absolute; left: 0; bottom: 0; width: 56%; height: 16px;
    background: var(--brand-blue);
  }
  .band-green {
    position: absolute; right: 0; bottom: 6px; width: 44%; height: 10px;
    background: var(--brand-green);
  }
</style>
</head>
<body>
<main class="canvas">
  <section class="card card--back" aria-label="Card back">
    <div class="wordmark">
      <span class="wordmark__dot"></span>
      <span>Wendleby Marsh<br>Consulting Limited</span>
    </div>
  </section>

  <section class="card card--front" aria-label="Card front">
    <div class="wordmark">
      <span class="wordmark__dot"></span>
      <span>Wendleby Marsh<br>Consulting Limited</span>
    </div>

    <div class="accent-marks" aria-hidden="true">
      <span class="accent-marks__green"></span>
      <span class="accent-marks__blue"></span>
    </div>

    <div class="person">
      <p class="person__name">Marcus Feldane</p>
      <p class="person__role">Director</p>
    </div>

    <ul class="contact-list">
      <li><span class="contact-list__tag">t</span><span class="contact-list__sep"></span>+44 7XXXXXXXXX</li>
      <li><span class="contact-list__tag">m</span><span class="contact-list__sep"></span>+44 7XXXXXXXXX</li>
      <li><span class="contact-list__tag">e</span><span class="contact-list__sep"></span>marcus@wendlebymarsh.com</li>
      <li><span class="contact-list__tag">w</span><span class="contact-list__sep"></span>www.wendlebymarsh.com</li>
    </ul>

    <div class="band-blue"></div>
    <div class="band-green"></div>
  </section>
</main>
</body>
</html>
```